Very visible CoWorking Building Sign overlooking downtown LA and 110 freeway

Our building is drab but very visible and in the best location. We need a great sign for our monolith that overlooks downtown LA and the 100 freeway. We are a new CoWorking business and would like to have a few things we do on the sign: private offices, virtual offices, CoWorking Lounge. Everything we have seen is ho-hum. Can you get us noticed? We need people to know what we do and that we are here but in a creative, professional, unique sign.
Target Market(s)
People who have a business in DTLA, remote workers and those who work from home who need a professional address.
Requirements
Must have
- Our logo (which can be somewhat reimagined) which has our address 2740 on it. The three things we focus on: Private Offices, Virtual Offices, CoWorking Lounge. Incorporate some Navy. Readable from several hundred feet away.
Nice to have
- Mural feel? Something inspirational in this crazy COVID times? Graphics? Color block. I like the idea of decorative but it has to be readable as a building sign. The same with the use of colors. Our colors are grays and navy but with a pop of the chartreuse (we have 2 velvet chartreuse chairs in the space). Helpful to view our website: Halvorn2740.com.
Should not have
- Not too graffiti. Keep it professional but unique and wow.

```html
<!DOCTYPE html>
<html lang="en">
<head>
<meta charset="utf-8">
<title>Halvorn 2740 Building Sign</title>
<link rel="stylesheet" href="https://fonts.googleapis.com/css2?family=Montserrat:wght@500;600;700&display=swap">
<style>
  :root {
    --navy: #0d3c7b;
    --navy-deep: #1b3563;
    --green-light: #9ccc3b;
    --green-dark: #74a912;
    --white: #ffffff;
    --backdrop-top: #bdbdbd;
    --backdrop-bottom: #f2f2f2;
  }
  * { margin: 0; padding: 0; box-sizing: border-box; }
  html, body {
    width: 720px;
    height: 1200px;
    overflow: hidden;
  }
  body {
    background: linear-gradient(180deg, var(--backdrop-top), var(--backdrop-bottom));
    display: flex;
    align-items: center;
    justify-content: center;
    font-family: "Montserrat", sans-serif;
  }
  .building-sign {
    display: block;
    width: 660px;
    height: 824px;
    box-shadow: 0 8px 18px rgba(0, 0, 0, 0.25);
  }
  .sign-brand {
    font-family: "Montserrat", sans-serif;
    font-weight: 500;
    font-size: 66px;
    fill: var(--navy-deep);
  }
  .service-label {
    font-family: "Montserrat", sans-serif;
    font-weight: 700;
    font-size: 39px;
    fill: var(--navy);
  }
  .sign-url {
    font-family: "Montserrat", sans-serif;
    font-weight: 600;
    font-size: 34px;
    letter-spacing: 4px;
    fill: var(--white);
  }
</style>
</head>
<body>
  <svg class="building-sign" viewBox="0 0 705 880" xmlns="http://www.w3.org/2000/svg" aria-labelledby="sign-title">
    <title id="sign-title">Halvorn 2740 – Private Offices, Virtual Offices, Coworking Lounge</title>

    <!-- Navy field -->
    <rect class="sign-field" width="705" height="880" fill="var(--navy)"/>

    <!-- Header swoosh: dark green, light green, white -->
    <path class="swoosh-shadow" fill="var(--green-dark)"
          d="M0,240 C170,350 350,472 525,474 C615,475 672,420 694,330 L705,300 L705,0 L0,0 Z"/>
    <path class="swoosh-edge" fill="var(--green-light)"
          d="M0,222 C170,338 380,412 560,398 C690,386 722,240 705,150 C694,90 668,34 640,0 L0,0 Z"/>
    <path class="swoosh-face" fill="var(--white)"
          d="M0,238 C170,335 380,398 550,388 C662,380 698,282 688,200 C678,122 640,52 598,0 L0,0 Z"/>

    <!-- Brand name -->
    <text class="sign-brand" x="345" y="250" text-anchor="middle">2740 HALVORN</text>

    <!-- Services list -->
    <g class="service-item">
      <rect x="95" y="490" width="550" height="66" rx="33" fill="var(--white)"/>
      <circle cx="95" cy="523" r="38" fill="var(--green-light)"/>
      <path d="M77,523 H111 M99,510 L112,523 L99,536" fill="none" stroke="var(--white)" stroke-width="6" stroke-linecap="round" stroke-linejoin="round"/>
      <text class="service-label" x="152" y="537">PRIVATE OFFICES</text>
    </g>
    <g class="service-item">
      <rect x="95" y="585" width="550" height="66" rx="33" fill="var(--white)"/>
      <circle cx="95" cy="618" r="38" fill="var(--green-light)"/>
      <path d="M77,618 H111 M99,605 L112,618 L99,631" fill="none" stroke="var(--white)" stroke-width="6" stroke-linecap="round" stroke-linejoin="round"/>
      <text class="service-label" x="155" y="632">VIRTUAL OFFICES</text>
    </g>
    <g class="service-item">
      <rect x="95" y="680" width="550" height="66" rx="33" fill="var(--white)"/>
      <circle cx="95" cy="713" r="38" fill="var(--green-light)"/>
      <path d="M77,713 H111 M99,700 L112,713 L99,726" fill="none" stroke="var(--white)" stroke-width="6" stroke-linecap="round" stroke-linejoin="round"/>
      <text class="service-label" x="152" y="727">COWORKING LOUNGE</text>
    </g>

    <!-- Web address band -->
    <rect class="url-band" x="0" y="784" width="705" height="60" fill="var(--green-light)"/>
    <text class="sign-url" x="352" y="826" text-anchor="middle">www.halvorn2740.com</text>
  </svg>
</body>
</html>
```